Rapid Rigworks One Page Email Template

The information and images in the attached file is correct. The logo, phone and web address have to remain at the top of the page. The customer thinks it's boring. I want to see how it can be made more lively using these same elements. Audience is auto industry. We're selling equipment for commercial vans. Size is 600 px wide. Nothing more to say.

Target Market(s)

Car and truck dealers and users.

Industry/Entity Type

Automotive

Font styles to use
Sans Serif

Requirements
Must have
• Elements in sample ... blue color in logo. Can be a combo with black and/or dark gray
Should not have
• Do not get too clever with colors. Blue and black are the company colors. You do not need to code the template. I just need a PSD.

```html
<!DOCTYPE html>
<html lang="en">
<head>
<meta charset="utf-8">
<title>Rapid Rigworks – Partitions Email</title>
<link rel="stylesheet" href="https://fonts.googleapis.com/css2?family=Figtree:wght@400;600;700;800;900&display=swap">
<style>
  :root {
    --brand-blue: #0a6bb8;
    --brand-blue-dark: #0758a0;
    --ink: #222222;
    --ink-soft: #555555;
    --text-muted: #8a8a8a;
    --band-grey: #ebebeb;
    --rule: #dcdcdc;
    --white: #ffffff;
  }
  * { box-sizing: border-box; margin: 0; padding: 0; }
  html, body { width: 1200px; height: 2216px; overflow: hidden; background: var(--white); }
  body { font-family: "Figtree", Arial, sans-serif; color: var(--ink); position: relative; }

  /* Header */
  .site-header { position: absolute; top: 0; left: 0; width: 1200px; height: 163px; }
  .brand { position: absolute; left: 400px; top: 22px; width: 420px; text-align: center; }
  .brand-row { display: flex; align-items: center; justify-content: center; gap: 14px; }
  .brand-mark { width: 34px; height: 34px; background: var(--brand-blue); }
  .brand-name { font-weight: 900; font-size: 50px; line-height: 1; color: var(--ink); letter-spacing: -0.5px; }
  .brand-tagline { margin-top: 10px; font-size: 13px; font-weight: 800; color: var(--ink); letter-spacing: 0.2px; }
  .header-phone { position: absolute; right: 28px; top: 62px; font-size: 25px; font-weight: 700; color: var(--brand-blue); }
  .rule-dark { position: absolute; left: 0; top: 142px; width: 996px; height: 8px; background: var(--ink); clip-path: polygon(0 0, 100% 0, 98.5% 100%, 0 100%); }
  .rule-blue { position: absolute; left: 0; top: 153px; width: 1200px; height: 5px; background: var(--brand-blue); }

  /* Hero */
  .hero { position: absolute; left: 0; top: 163px; width: 1200px; height: 549px; }
  .hero-photo { position: absolute; inset: 0;
    background: linear-gradient(180deg, #6f8a5c 0%, #8fa873 22%, #cfd4d6 40%, #e6e8ea 62%, #b8bbbc 100%); }
  .hero-banner { position: absolute; left: 0; top: 197px; width: 572px; height: 127px; background: var(--brand-blue);
    color: var(--white); font-weight: 800; font-size: 39px; line-height: 51px; padding: 11px 0 0 52px; text-transform: uppercase; }
  .partner-badge { position: absolute; left: 980px; top: 255px; width: 170px; height: 26px; background: #111111; }

  /* Welcome */
  .welcome { position: absolute; left: 0; top: 712px; width: 1200px; height: 240px; text-align: center; }
  .section-title { font-size: 38px; font-weight: 700; text-transform: uppercase; letter-spacing: 0.5px; }
  .section-title .accent { color: var(--brand-blue); }
  .welcome .section-title { margin-top: 40px; color: var(--ink-soft); }
  .welcome .section-title .accent { font-size: 41px; }
  .lede { font-family: Arial, Helvetica, sans-serif; font-size: 18px; line-height: 31px; color: var(--text-muted); width: 700px; margin: 22px auto 0; }
  .lede a { color: var(--brand-blue); font-weight: 700; text-decoration: none; font-family: "Figtree", Arial, sans-serif; }

  /* Services */
  .services { position: absolute; left: 0; top: 952px; width: 1200px; height: 803px; background: var(--band-grey); text-align: center; }
  .services .section-title { margin-top: 46px; color: var(--ink); font-size: 35px; }
  .services .lede { margin-top: 14px; width: 680px; }
  .service-grid { position: absolute; left: 249px; top: 194px; width: 702px; display: grid; grid-template-columns: 338px 338px; column-gap: 24px; row-gap: 26px; }
  .service-tile { position: relative; height: 221px; }
  .service-image { position: absolute; inset: 0; background: radial-gradient(ellipse at center, #6fa4d3 0%, #2f7fc3 55%, #1b68ad 100%); }
  .service-label { position: absolute; inset: 0; display: flex; align-items: center; justify-content: center;
    color: var(--white); font-weight: 700; font-size: 23px; line-height: 29px; text-transform: uppercase; }
  .cta { position: absolute; left: 465px; top: 705px; width: 279px; height: 47px; border-radius: 24px; background: var(--brand-blue-dark);
    color: var(--white); font-weight: 700; font-size: 22px; line-height: 47px; text-transform: uppercase; text-decoration: none; }

  /* Footer */
  .site-footer { position: absolute; left: 0; top: 1755px; width: 1200px; height: 461px; text-align: center; }
  .footer-note { margin-top: 68px; font-size: 24px; font-weight: 600; color: var(--text-muted); }
  .footer-web { margin-top: 12px; font-size: 31px; font-weight: 700; color: var(--brand-blue); }
  .footer-rule { width: 656px; height: 1px; background: var(--rule); margin: 24px auto 0; }
  .office-title { margin-top: 24px; font-size: 24px; font-weight: 700; color: var(--ink); text-transform: uppercase; }
  .office-line { margin-top: 10px; font-size: 20px; color: var(--ink-soft); line-height: 26px; }
  .office-line .label { color: var(--brand-blue); font-weight: 700; }
  .follow-title { margin-top: 26px; font-size: 24px; font-weight: 700; color: var(--brand-blue); }
  .social-row { display: flex; justify-content: center; gap: 8px; margin-top: 18px; }
  .social-dot { width: 28px; height: 28px; border-radius: 50%; background: #6e6e6e; }
</style>
</head>
<body>
  <header class="site-header">
    <div class="brand">
      <div class="brand-row"><span class="brand-mark"></span><span class="brand-name">Rapid Rigworks</span></div>
      <div class="brand-tagline">YOUR RAPID SOURCE FOR COMMERCIAL VAN &amp; LIGHT TRUCK EQUIPMENT</div>
    </div>
    <div class="header-phone">Call us : (800) 555-0142</div>
    <div class="rule-dark"></div>
    <div class="rule-blue"></div>
  </header>

  <section class="hero">
    <div class="hero-photo" role="img" aria-label="White commercial van with a ladder rack parked in front of a house and lawn"></div>
    <h1 class="hero-banner">Partitions available<br>for select vans</h1>
    <div class="partner-badge" role="img" aria-label="Partner badge"></div>
  </section>

  <section class="welcome">
    <h2 class="section-title">Welcome to <span class="accent">Rapid Rigworks</span></h2>
    <p class="lede">Lorem ipsum dolor sit amet, consectetur adipiscing elit. Etiam ante urna, placerat eu euismod dictum, aliquam et sapien. Ut at risus commodo, eleifend sem cursus Lorem ipsum dolor sit amet, consectetur adipiscing elit. <a href="#">Read More...</a></p>
  </section>

  <section class="services">
    <h2 class="section-title">Offered <span class="accent">Services</span></h2>
    <p class="lede">Lorem ipsum dolor sit amet, consectetur adipiscing elit. Etiam ante urna, placerat eu euismod dictum, aliquam et sapien. Ut at risus commodo, eleifend sem cursus</p>
    <div class="service-grid">
      <div class="service-tile">
        <div class="service-image" role="img" aria-label="Empty cargo area of a low roof van"></div>
        <div class="service-label">Vantrek Cargo<br>Low Roof Partition</div>
      </div>
      <div class="service-tile">
        <div class="service-image" role="img" aria-label="Partition wall with window inside a compact van"></div>
        <div class="service-label">Vantrek Compact<br>Partition</div>
      </div>
      <div class="service-tile">
        <div class="service-image" role="img" aria-label="Cargo area of a low roof van seen from the rear doors"></div>
        <div class="service-label">Vantrek Cargo<br>Low Roof Partition</div>
      </div>
      <div class="service-tile">
        <div class="service-image" role="img" aria-label="Solid partition inside a compact van"></div>
        <div class="service-label">Vantrek Compact<br>Partition</div>
      </div>
    </div>
    <a class="cta" href="#">Register Hurry Up</a>
  </section>

  <footer class="site-footer">
    <p class="footer-note">Call your local Rapid Rigworks Office for detailsd and availability</p>
    <p class="footer-web">www.rapidrigworks.com</p>
    <div class="footer-rule"></div>
    <h3 class="office-title">Our Corporate Office</h3>
    <p class="office-line">418 N. Delmar Ave. Fontana, CA 92335</p>
    <p class="office-line"><span class="label">Email :</span> info@rapidrigworks.com</p>
    <p class="office-line"><span class="label">Call :</span> (800) 555-0142</p>
    <div class="footer-rule"></div>
    <p class="follow-title">Follow us</p>
    <div class="social-row">
      <span class="social-dot" aria-label="Social link"></span>
      <span class="social-dot" aria-label="Social link"></span>
      <span class="social-dot" aria-label="Social link"></span>
    </div>
  </footer>
</body>
</html>
```